Washington DC Solo Practitioner Law Firm needs Stationery and Business Card Design

We need a letterhead and business card for a new law firm based in Washington DC called Harlow PLLC. The law firm is a single lawyer practicing appellate law (U.S. Supreme Court, Federal District Courts, State Supreme Courts).
We already have a logo designed through a MarkHive contest. The letterhead and the business card should include the Logo and have the same look and feel as the Logo - same fonts and colors, please. We would like a clean, crisp, simple, professional look. The design should convey stability and experience.
We have .png and .psd and .ai files for the logo, as needed
Dark blue color is PANTONE P 108-16 C
Grey color is PANTONE P 179-11 C
Type face is Century Gothic Regular typeface

```html
<!DOCTYPE html>
<html lang="en">
<head>
<meta charset="utf-8">
<title>Harlow PLLC — Business Card</title>
<link href="https://fonts.googleapis.com/css2?family=Didact+Gothic&family=Nunito+Sans:wght@800&display=swap" rel="stylesheet">
<style>
  :root {
    --navy: #123f74;
    --navy-deep: #0e3566;
    --grey: #6f6f70;
    --paper: #f4f4f2;
    --backdrop: #d6d6d6;
    --white: #ffffff;
  }
  * { margin: 0; padding: 0; box-sizing: border-box; }
  html, body { width: 1200px; height: 720px; overflow: hidden; }
  body {
    background: var(--backdrop);
    font-family: "Didact Gothic", "Century Gothic", sans-serif;
    position: relative;
  }
  .card {
    position: absolute;
    top: 205px;
    width: 540px;
    height: 309px;
    box-shadow: 0 6px 18px rgba(0,0,0,0.18);
  }
  .card--front { left: 40px; background: var(--paper); color: var(--grey); }
  .card--back { left: 620px; background: var(--navy); color: var(--white); }

  .brand { position: absolute; display: flex; align-items: flex-start; gap: 14px; }
  .brand__mark { width: 34px; height: 34px; flex: none; margin-top: 2px; }
  .brand__name { font-size: 34px; letter-spacing: 1px; line-height: 1; }
  .brand__tagline { font-size: 8px; letter-spacing: 0.6px; text-transform: uppercase; margin-top: 6px; }

  .card--front .brand { left: 40px; top: 38px; }
  .card--front .brand__mark { background: var(--navy); }
  .card--front .brand__name { color: var(--navy); }
  .card--front .brand__tagline { color: var(--grey); }

  .card--back .brand { left: 150px; top: 110px; }
  .card--back .brand__mark { background: var(--white); }
  .card--back .brand__name, .card--back .brand__tagline { color: var(--white); }
  .website { font-size: 15px; letter-spacing: 1.5px; margin-top: 10px; }
  .website b { font-weight: normal; letter-spacing: 2px; }

  .person {
    position: absolute; left: 40px; top: 132px;
    font-family: "Nunito Sans", sans-serif; font-weight: 800;
    font-size: 19px; color: var(--navy);
  }
  .address {
    position: absolute; left: 40px; top: 170px;
    display: flex; gap: 8px; font-size: 14px; line-height: 1.35;
  }
  .contacts {
    position: absolute; left: 215px; top: 218px;
    font-size: 14px; line-height: 1.45; list-style: none;
  }
  .contacts li { display: flex; align-items: center; gap: 10px; }
  .icon { width: 12px; height: 12px; flex: none; fill: var(--navy); }
  .address .icon { margin-top: 3px; }
</style>
</head>
<body>
  <section class="card card--front" aria-label="Business card front">
    <div class="brand">
      <span class="brand__mark"></span>
      <div>
        <div class="brand__name">HARLOW PLLC</div>
        <div class="brand__tagline">Trial and Appellate Litigation</div>
      </div>
    </div>
    <p class="person">Evan Harlow</p>
    <div class="address">
      <svg class="icon" viewBox="0 0 12 12" aria-hidden="true"><path d="M6 0a4 4 0 0 0-4 4c0 3 4 8 4 8s4-5 4-8a4 4 0 0 0-4-4zm0 5.6A1.6 1.6 0 1 1 6 2.4a1.6 1.6 0 0 1 0 3.2z"/></svg>
      <p>2210 M Street NW,<br>Suite 400<br>Washington, DC 20037</p>
    </div>
    <ul class="contacts">
      <li><svg class="icon" viewBox="0 0 12 12" aria-hidden="true"><path d="M1 3c0-1 1-2 5-2s5 1 5 2v1H8V3H4v1H1zM2 5h8l1 6H1z"/></svg>202-555-0148</li>
      <li><svg class="icon" viewBox="0 0 12 12" aria-hidden="true"><rect x="3" y="0" width="6" height="12" rx="1"/><rect x="4" y="1.5" width="4" height="7" fill="#f4f4f2"/></svg>571-555-0193</li>
      <li><svg class="icon" viewBox="0 0 12 12" aria-hidden="true"><path d="M0 2h12v8H0z"/><path d="M0.5 2.5L6 7l5.5-4.5" stroke="#f4f4f2" fill="none"/></svg>eharlow@harlowpllc.com</li>
    </ul>
  </section>

  <section class="card card--back" aria-label="Business card back">
    <div class="brand">
      <span class="brand__mark"></span>
      <div>
        <div class="brand__name">HARLOW PLLC</div>
        <div class="brand__tagline">Trial and Appellate Litigation</div>
        <div class="website">www.<b>harlowpllc</b>.com</div>
      </div>
    </div>
  </section>
</body>
</html>
```